Rulo Pantryware Sous Vide Cooker PRODUCT PACKAGING design

We need a product packaging design for our current brand. We are a growing kitchen brand that focuses on slick and professional appliances.

We would like designs that use either black/white/ or silver, some other colors could also be added but we would like our designs to be slick and professional.

We have attached a .txt file that explains the text that should be added and also have attached all of our stock images.

We need our logo to be Photoshopped into the images to replace the current logo. Our logo can be tweaked into something simpler like just the "R&P" to fit our product if needed.

Please refer to the link for the pictures (I could not upload them here because of size)
https://files.brivostore.net/share/7QwXe2LmTzRkVa9PnHc4YbUdJf0?view=open

Target Market(s)

Kitchen Tralvo Customers

Industry/Entity Type

Kitchen

Font styles to use
Serif

Colors
0792cd
000000
ffffff

Requirements
Must have
• Everything this is pointed out in the text file, professional look, yet simple. We try to model our products off of the Brand Karvel and how they package their products
Nice to have
• look at Karvel as an example of quality
Should not have
• cheesy designs that look unprofessional

```html
<!DOCTYPE html>
<html lang="en">
<head>
<meta charset="utf-8">
<title>Rulo Pantryware Sous Vide 2.0 – Box Dieline</title>
<link href="https://fonts.googleapis.com/css2?family=Libre+Baskerville&family=Questrial&family=Great+Vibes&family=Oswald:wght@300&display=swap" rel="stylesheet">
<style>
  :root {
    --ink: #000000;
    --panel-dark: #1c1c1c;
    --paper: #ffffff;
    --accent: #0792cd;
    --cut-line: #9a9a9a;
    --muted: #6e6e6e;
    --gold: #c9a43a;
  }
  html, body {
    margin: 0;
    width: 1200px;
    height: 1154px;
    overflow: hidden;
    background: var(--paper);
  }
  .dieline { display: block; width: 1200px; height: 1154px; }
  .cut { fill: none; stroke: var(--cut-line); stroke-width: 1.2; }
  .panel-dark { fill: var(--panel-dark); }
  .panel-light { fill: var(--paper); }
  .brand { font-family: "Libre Baskerville", serif; letter-spacing: 3px; }
  .brand--light { fill: var(--paper); }
  .brand--dark { fill: var(--ink); }
  .size-label { font-family: "Questrial", sans-serif; font-size: 24px; fill: var(--muted); letter-spacing: 2px; }
  .body-copy { font-family: "Questrial", sans-serif; font-size: 16px; }
  .body-copy--light { fill: var(--paper); }
  .body-copy--dark { fill: #222; }
  .script { font-family: "Great Vibes", cursive; fill: var(--paper); }
  .product-name { font-family: "Oswald", sans-serif; font-weight: 300; font-size: 38px; fill: #1a1a1a; }
  .product-version { font-family: "Great Vibes", cursive; font-size: 48px; fill: var(--accent); }
  .icon { fill: none; stroke: var(--paper); stroke-width: 3; stroke-linecap: round; stroke-linejoin: round; }
</style>
</head>
<body>
<svg class="dieline" viewBox="0 0 1500 1442" xmlns="http://www.w3.org/2000/svg">
  <defs>
    <linearGradient id="productTone" x1="0" y1="0" x2="1" y2="0">
      <stop offset="0" stop-color="#2d2f31"/>
      <stop offset="0.5" stop-color="#6f7275"/>
      <stop offset="1" stop-color="#2a2c2e"/>
    </linearGradient>
    <linearGradient id="mealTone" x1="0" y1="0" x2="1" y2="1">
      <stop offset="0" stop-color="#e8e6e3"/>
      <stop offset="0.4" stop-color="#8a5a48"/>
      <stop offset="0.7" stop-color="#c98a82"/>
      <stop offset="1" stop-color="#d9d6d2"/>
    </linearGradient>
    <radialGradient id="goldTone">
      <stop offset="0" stop-color="#e9cf78"/>
      <stop offset="1" stop-color="var(--gold)"/>
    </radialGradient>
  </defs>

  <text class="size-label" x="855" y="98">205×110×425</text>

  <!-- Top lid flap -->
  <path class="cut" d="M78 70 L78 42 Q78 28 92 28 L512 28 Q526 28 526 42 L526 70"/>
  <rect class="panel-dark" x="75" y="70" width="452" height="242"/>
  <circle cx="295" cy="185" r="40" fill="none" stroke="var(--paper)" stroke-width="2"/>
  <text class="brand brand--light" x="296" y="244" font-size="16" text-anchor="middle">Rulo Pantryware</text>

  <!-- Glue flap -->
  <path class="cut" d="M75 316 L32 322 L32 1244 L75 1250"/>

  <!-- Front panel -->
  <rect class="panel-light cut" x="75" y="312" width="452" height="938"/>
  <circle cx="188" cy="388" r="40" fill="var(--ink)"/>
  <text class="brand brand--dark" x="188" y="447" font-size="16" text-anchor="middle">Rulo Pantryware</text>
  <circle cx="440" cy="392" r="52" fill="url(#goldTone)" role="img" aria-label="One year warranty seal"/>
  <rect x="187" y="470" width="226" height="654" fill="url(#productTone)" rx="40" role="img" aria-label="Photo of the sous vide immersion cooker with digital display"/>
  <text x="281" y="1215"><tspan class="product-name">SOUS VIDE</tspan><tspan class="product-version" dx="6">2.0</tspan></text>

  <!-- Left side panel -->
  <path class="cut" d="M534 312 L534 185 L730 185 L768 300 L768 312"/>
  <rect class="panel-dark" x="530" y="315" width="238" height="935"/>
  <circle cx="648" cy="560" r="32" fill="none" stroke="var(--paper)" stroke-width="2"/>
  <text class="brand brand--light" x="648" y="605" font-size="12" text-anchor="middle">Rulo Pantryware</text>
  <text class="body-copy body-copy--light" text-anchor="middle">
    <tspan x="648" y="672">Everything we do is to</tspan>
    <tspan x="648" dy="22.5">encourage people to</tspan>
    <tspan x="648" dy="22.5">become more</tspan>
    <tspan x="648" dy="22.5">advance in their</tspan>
    <tspan x="648" dy="22.5">culinary arts. We do</tspan>
    <tspan x="648" dy="22.5">this by making</tspan>
    <tspan x="648" dy="22.5">products beautifully</tspan>
    <tspan x="648" dy="22.5">designed, simple to</tspan>
    <tspan x="648" dy="22.5">use, and user friendly.</tspan>
    <tspan x="648" dy="22.5">We just happen to</tspan>
    <tspan x="648" dy="22.5">make the highest</tspan>
    <tspan x="648" dy="22.5">quality kitchen</tspan>
    <tspan x="648" dy="22.5">products on the</tspan>
    <tspan x="648" dy="22.5">market.</tspan>
  </text>

  <!-- Back panel -->
  <path class="cut" d="M943 372 L943 278 Q943 262 959 262 L1037 262 Q1053 262 1053 278 L1053 372 Z"/>
  <line class="cut" x1="943" y1="316" x2="1053" y2="316"/>
  <rect class="panel-light cut" x="770" y="315" width="455" height="935"/>
  <text class="body-copy body-copy--dark">
    <tspan x="792" y="420">You’re not far from the best steak you’ll ever</tspan>
    <tspan x="792" dy="22.5">have! Our personal favorite is our New York Strip</tspan>
    <tspan x="792" dy="22.5">recipe, which you’ll find in our cook book. If not</tspan>
    <tspan x="792" dy="22.5">a fan of steaks, there are many other recipes in</tspan>
    <tspan x="792" dy="22.5">our cook book. Please let us know how your</tspan>
    <tspan x="792" dy="22.5">meals turned out!</tspan>
    <tspan x="792" dy="45">DON’T FORGET to register your product on</tspan>
    <tspan x="792" dy="22.5">www.rulopantryware.com for your 1 year</tspan>
    <tspan x="792" dy="22.5">warranty!</tspan>
  </text>
  <rect x="770" y="770" width="455" height="416" fill="url(#mealTone)" role="img" aria-label="Photo of sliced sous vide steak with green beans on a white plate"/>

  <!-- Right side panel -->
  <path class="cut" d="M1228 312 L1228 300 L1266 185 L1460 185 L1460 312"/>
  <rect class="panel-dark" x="1225" y="315" width="238" height="935"/>
  <text class="script" x="1350" y="455" font-size="46" text-anchor="middle">4 steps:</text>
  <text class="script" x="1350" y="557" font-size="38" text-anchor="middle">1.Prepare</text>
  <g class="icon" role="img" aria-label="Seasoning shaker icon">
    <rect x="1338" y="585" width="22" height="30" rx="4" transform="rotate(35 1349 600)"/>
    <circle cx="1328" cy="630" r="1.5"/><circle cx="1336" cy="636" r="1.5"/>
  </g>
  <text class="script" x="1345" y="717" font-size="38" text-anchor="middle">2.Package</text>
  <g class="icon" role="img" aria-label="Vacuum bag icon">
    <rect x="1328" y="743" width="46" height="52" rx="3"/>
    <line x1="1328" y1="752" x2="1374" y2="752"/>
    <rect x="1331" y="770" width="40" height="22" fill="var(--paper)" stroke="none"/>
  </g>
  <text class="script" x="1340" y="888" font-size="38" text-anchor="middle">3.Cook</text>
  <g class="icon" role="img" aria-label="Cooking pot icon">
    <path d="M1324 946 L1380 946 M1330 946 L1330 982 L1374 982 L1374 946"/>
    <path d="M1345 946 L1345 918 Q1345 905 1355 908"/>
  </g>
  <text class="script" x="1345" y="1058" font-size="38" text-anchor="middle">4.Enjoy!</text>
  <g class="icon" role="img" aria-label="Served plate icon">
    <ellipse cx="1350" cy="1112" rx="36" ry="16"/>
    <ellipse cx="1350" cy="1106" rx="14" ry="8"/>
  </g>

  <!-- Bottom flaps -->
  <path class="cut" d="M78 1250 L78 1402 Q78 1416 92 1416 L186 1416 L186 1372 L416 1372 L416 1416 L512 1416 Q526 1416 526 1402 L526 1250"/>
  <path class="cut" d="M530 1250 L530 1300 L650 1416 L768 1416 L768 1250"/>
  <path class="cut" d="M770 1250 L885 1372 L885 1416 L1110 1416 L1110 1372 L1225 1250"/>
  <path class="cut" d="M1228 1250 L1228 1416 L1344 1416 L1344 1365 L1460 1300 L1460 1250"/>
</svg>
</body>
</html>
```